Wedding and event Photography company.

We need a business card design for a photography company based in Singapore named TamKeza. Our core service offering is wedding photojournalism. We would like to see minimalistic designs that use the colour white. The final design should communicate a sense of ease and reliability.

The attached are a couple of visual reference which i found over the web, i hope it will helps.

Project Brief Update (14th July 2014):
- Please refrain from using any images from the website for the design. The laws and regulations over here does not allow me to distribute my client's images. Thanks!

Target Market(s)

Young and middle aged adults aged 24 - 38. With money to spend =D

Industry/Entity Type

Business

Contact Information for Business Card

Name: Dev Lunor
Designation: Head Photographer
Mobile: +65 81749026
Email: jun@tamkeza.example
Website: www.tamkeza.example

Font styles to use
Other font styles liked:
• Baskerville URW

Colors

Designer to choose colors to be used in the design.

Requirements
Must have
• Must include:
• - The brand TamKeza
• - The logo attached
• - Please help to place the brand TamKeza with the logo according to your preferences.
• - Services
• - Wedding Photography
• - Portraiture
• - Photojournalism
Nice to have
• Looking forward to an elegant and simple design. Please see attached examples!
• Please use Serif Fonts
Should not have
• Please refrain from using dark tones for the majority of the design.
• Please refrain from letterpress and embossing.

```html
<!DOCTYPE html>
<html lang="en">
<head>
<meta charset="utf-8">
<title>TamKeza Business Card</title>
<link rel="stylesheet" href="https://fonts.googleapis.com/css2?family=Libre+Baskerville:wght@400&family=Jost:wght@400&display=swap">
<style>
  :root {
    --page-bg: #f0f0f0;
    --card-bg: #e5e4eb;
    --ink: #141414;
    --card-edge: #d6d5dc;
  }
  * { margin: 0; padding: 0; box-sizing: border-box; }
  html, body {
    width: 1200px;
    height: 1000px;
    overflow: hidden;
    background: var(--page-bg);
  }
  .canvas {
    position: relative;
    width: 1200px;
    height: 1000px;
  }
  .card {
    position: absolute;
    left: 283px;
    width: 659px;
    height: 376px;
    background: var(--card-bg);
    border: 1px solid var(--card-edge);
    color: var(--ink);
    font-family: "Libre Baskerville", "Baskerville", serif;
  }
  .card--front { top: 91px; }
  .card--back { top: 574px; }

  .name-frame {
    position: absolute;
    left: 136px;
    top: 138px;
    width: 386px;
    height: 100px;
    border: 2px solid var(--ink);
    text-align: center;
  }
  .name-frame .holder-name {
    margin-top: 17px;
    font-size: 32px;
    line-height: 38px;
    letter-spacing: 0.3em;
    padding-left: 0.3em;
  }
  .name-frame .holder-role {
    margin-top: 3px;
    font-size: 17px;
    line-height: 24px;
    letter-spacing: 0.22em;
    padding-left: 0.22em;
  }

  .service-list {
    position: absolute;
    left: 0;
    right: 0;
    top: 262px;
    display: flex;
    justify-content: center;
    gap: 26px;
    list-style: none;
    font-family: "Jost", "Futura", sans-serif;
    font-size: 12px;
    line-height: 16px;
    letter-spacing: 0.2em;
    text-transform: uppercase;
  }

  .brand-name {
    position: absolute;
    left: 400px;
    top: 88px;
    font-size: 28px;
    letter-spacing: 0.08em;
  }

  .holder-block {
    position: absolute;
    left: 46px;
    top: 222px;
  }
  .holder-block .holder-name {
    font-size: 25px;
    line-height: 30px;
    letter-spacing: 0.12em;
  }
  .holder-block .holder-role {
    font-size: 14px;
    line-height: 16px;
    letter-spacing: 0.14em;
  }

  .contact-list {
    position: absolute;
    left: 400px;
    top: 224px;
    font-family: "Jost", "Futura", sans-serif;
    font-size: 13px;
    line-height: 18.5px;
    letter-spacing: 0.2em;
    list-style: none;
  }
  .contact-list .reg-number { margin-top: 18px; }
</style>
</head>
<body>
<main class="canvas">
  <section class="card card--front" aria-label="Card front">
    <div class="name-frame">
      <p class="holder-name">Dev Lunor</p>
      <p class="holder-role">Head Photographer</p>
    </div>
    <ul class="service-list" aria-label="Services">
      <li>Wedding Photography</li>
      <li>Portraiture</li>
      <li>Photojournalism</li>
    </ul>
  </section>

  <section class="card card--back" aria-label="Card back">
    <p class="brand-name">TamKeza</p>
    <div class="holder-block">
      <p class="holder-name">Dev Lunor</p>
      <p class="holder-role">Head Photographer</p>
    </div>
    <ul class="contact-list">
      <li>Tel: +65 81749026</li>
      <li>Email: jun@tamkeza.example</li>
      <li>Web: tamkeza.example</li>
      <li class="reg-number">Reg No: 61847209K</li>
    </ul>
  </section>
</main>
</body>
</html>
```